Private Investigator needs business card with an intelligent logo

Private Investigator needs uncluttered, intelligently designed business card with simple logo. Prefer one or two colour print only. Must convey serious approach with only basic information: Business Name, "Clearwater Inquiries"
Phone: 03 4196 5031 Email: info@clear-water.example.com.au Web: www.clear-water.example.com.au
Agents Name: Gavin Thornley Title: Investigator Mobile: 0417 263 594

Thank you all very much for your designs.  There was some really excellent ideas and the choice was very hard.  I sought opinions from a number of people about which was the best one and there were a number of different choices but eventually the majority went with one design from Rovelko.  Thank you especially to those designers that made some changes when I suggested them.

Thanks again for all your efforts and good luck with your design careers.  I will certainly use SketchMarket again with the great quality of designers that made submissions.

Regards  Gavin Thornley

```html
<!DOCTYPE html>
<html lang="en">
<head>
<meta charset="utf-8">
<title>Clearwater Inquiries – Business Card</title>
<link rel="stylesheet" href="https://fonts.googleapis.com/css2?family=Didact+Gothic&display=swap">
<style>
  :root {
    --backdrop: #d9d6d2;
    --card-core: #1e1e1e;
    --card-edge: #050505;
    --ink: #f2f2f2;
    --ink-soft: #c9c9c9;
    --rule: #ffffff;
  }
  * { margin: 0; padding: 0; box-sizing: border-box; }
  html, body {
    width: 1200px;
    height: 960px;
    overflow: hidden;
    background: var(--backdrop);
  }
  .canvas {
    width: 1200px;
    height: 960px;
    display: flex;
    flex-direction: column;
    align-items: center;
    justify-content: center;
    gap: 56px;
  }
  .card {
    position: relative;
    width: 660px;
    height: 404px;
    background: radial-gradient(ellipse at 50% 45%, var(--card-core) 0%, var(--card-edge) 75%);
    box-shadow: 0 10px 30px rgba(0,0,0,0.25);
    font-family: "Didact Gothic", "Helvetica Neue", Arial, sans-serif;
    color: var(--ink);
  }
  .brand {
    position: absolute;
    display: flex;
    flex-direction: column;
    align-items: center;
    gap: 14px;
  }
  .brand-mark {
    width: 54px;
    height: 54px;
    border: 3px solid var(--ink);
    border-radius: 50%;
  }
  .brand-name {
    font-size: 24px;
    letter-spacing: 0.3px;
    color: var(--ink);
    white-space: nowrap;
  }
  .card--front .brand {
    left: 50%;
    top: 50%;
    transform: translate(-50%, -50%);
  }
  .card--back .brand {
    left: 70px;
    top: 140px;
  }
  .contact {
    position: absolute;
    left: 400px;
    top: 34px;
    padding-left: 14px;
    border-left: 3px solid var(--rule);
    font-size: 14px;
    line-height: 1.5;
    color: var(--ink-soft);
  }
  .contact-name {
    font-size: 19px;
    color: var(--ink);
    line-height: 1.3;
  }
</style>
</head>
<body>
  <main class="canvas">
    <section class="card card--front" aria-label="Business card front">
      <div class="brand">
        <span class="brand-mark"></span>
        <span class="brand-name">Clearwater Inquiries</span>
      </div>
    </section>

    <section class="card card--back" aria-label="Business card back">
      <div class="brand">
        <span class="brand-mark"></span>
        <span class="brand-name">Clearwater Inquiries</span>
      </div>
      <div class="contact">
        <p class="contact-name">Gavin Thornley</p>
        <p>Investigator Mobile: 0417 263 594</p>
        <p>Email: info@clear-water.example.com.au</p>
        <p>Web: www.clear-water.example.com.au</p>
        <p>Phone: 03 4196 5031</p>
      </div>
    </section>
  </main>
</body>
</html>
```